Keystone Facility Partners Business card

We wish to have a professional Business card to present to large Corporate CEO's ASAP.

Our web site helps explain our business www.keystonefp.org

Keystone Facility Partners was established after we discovered how difficult it is to organise outsourced services while heading up a business or company.

We act as a facilitator for businesses who don't have the desire, expertise or recourses to manage their own systems and meet all their requirements.

We provide an all in one facility management solution for all types of businesses. We manage schedules, contractors and costs on behalf of businesses and their needs and wants.

Having an extensive network ensures we are able to connect businesses with the right service providers.

Target Market(s)

Company CEO

Industry/Entity Type

Business

Font styles to use
Sans Serif

Colors
33a6d7
f9fdfe
0355a3

Requirements
Must have
• professional design
Nice to have
• colours to match logo

```html
<!DOCTYPE html>
<html lang="en">
<head>
<meta charset="utf-8">
<title>Keystone Facility Partners – Business Card</title>
<link rel="stylesheet" href="https://fonts.googleapis.com/css2?family=Arimo:wght@400;700&display=swap">
<style>
  :root {
    --sky: #33a6d7;
    --paper: #f9fdfe;
    --navy: #0355a3;
    --ink: #1c1c1c;
    --stage: #e9edf0;
  }
  * { box-sizing: border-box; margin: 0; padding: 0; }
  html, body { width: 1200px; height: 1000px; overflow: hidden; }
  body {
    background: var(--stage);
    font-family: "Arimo", Arial, sans-serif;
    position: relative;
  }
  .card {
    position: absolute;
    left: 200px;
    width: 800px;
    height: 457px;
    border-radius: 4px;
    box-shadow: 0 6px 18px rgba(0,0,0,.15);
    overflow: hidden;
  }
  /* Front face */
  .card--front {
    top: 32px;
    background: radial-gradient(ellipse at 55% 45%, #39a9dc 0%, #1f86c7 45%, var(--navy) 100%);
  }
  .front-brand {
    position: absolute;
    left: 140px;
    top: 195px;
    display: flex;
    align-items: center;
    gap: 18px;
  }
  .front-brand .brand-dot {
    width: 44px; height: 44px; border-radius: 50%;
    background: rgba(255,255,255,.85);
  }
  .front-brand .brand-name {
    color: #fff;
    font-weight: 400;
    font-size: 34px;
    letter-spacing: 3px;
    text-transform: uppercase;
  }
  /* Back face */
  .card--back {
    top: 511px;
    background: var(--paper);
  }
  .back-brand {
    position: absolute;
    right: 40px;
    top: 48px;
    display: flex;
    align-items: center;
    gap: 12px;
  }
  .back-brand .brand-dot {
    width: 30px; height: 30px; border-radius: 50%;
    background: var(--navy);
  }
  .back-brand .brand-name {
    color: var(--navy);
    font-weight: 400;
    font-size: 23px;
    letter-spacing: 2px;
    text-transform: uppercase;
  }
  .divider {
    position: absolute;
    left: 0; right: 0;
    top: 118px;
    height: 6px;
    border-top: 2px solid var(--sky);
    border-bottom: 1.5px solid var(--navy);
  }
  .holder {
    position: absolute;
    left: 70px;
    top: 172px;
  }
  .holder-name {
    font-size: 40px;
    font-weight: 400;
    color: var(--navy);
    margin-bottom: 18px;
  }
  .contact-list { list-style: none; }
  .contact-list li {
    display: flex;
    align-items: center;
    gap: 10px;
    font-size: 22px;
    color: var(--ink);
    margin-bottom: 12px;
  }
  .contact-list svg { width: 18px; height: 18px; flex: none; }
</style>
</head>
<body>
  <section class="card card--front" aria-label="Card front">
    <div class="front-brand">
      <span class="brand-dot"></span>
      <span class="brand-name">Keystone Facility Partners</span>
    </div>
  </section>

  <section class="card card--back" aria-label="Card back">
    <div class="back-brand">
      <span class="brand-dot"></span>
      <span class="brand-name">Keystone Facility Partners</span>
    </div>
    <div class="divider"></div>
    <div class="holder">
      <h1 class="holder-name">Lena Marsh</h1>
      <ul class="contact-list">
        <li>
          <svg viewBox="0 0 24 24" aria-hidden="true"><path fill="#1c1c1c" d="M6.6 10.8c1.4 2.8 3.8 5.1 6.6 6.6l2.2-2.2c.3-.3.7-.4 1-.2 1.1.4 2.3.6 3.6.6.6 0 1 .4 1 1V20c0 .6-.4 1-1 1C10.6 21 3 13.4 3 4c0-.6.4-1 1-1h3.5c.6 0 1 .4 1 1 0 1.3.2 2.5.6 3.6.1.3 0 .7-.2 1z"/></svg>
          <span>0410 555 218</span>
        </li>
        <li>
          <svg viewBox="0 0 24 24" aria-hidden="true"><rect x="2.5" y="5" width="19" height="14" fill="none" stroke="#1c1c1c" stroke-width="1.6"/><path d="M2.5 5l9.5 8 9.5-8" fill="none" stroke="#1c1c1c" stroke-width="1.6"/></svg>
          <span>lena@keystonefp.org</span>
        </li>
        <li>
          <svg viewBox="0 0 24 24" aria-hidden="true"><circle cx="12" cy="12" r="9.5" fill="none" stroke="#1c1c1c" stroke-width="1.6"/><ellipse cx="12" cy="12" rx="4" ry="9.5" fill="none" stroke="#1c1c1c" stroke-width="1.4"/><path d="M2.5 12h19" stroke="#1c1c1c" stroke-width="1.4"/></svg>
          <span>www.keystonefp.org</span>
        </li>
      </ul>
    </div>
  </section>
</body>
</html>
```